High-Converting Facebook Ads for Panes Screens & Louvres (6 Products)

We are looking for a graphic designer to create high-quality Facebook & Instagram ads for our business: Panes Screens and Louvres (Melbourne, Australia).

We require 6 separate ad designs, each for a different product:

Veltrashade Blinds

Outdoor Awnings

Plantation Shutters

Roller Shutters

Security Doors

Roller Blinds & Sheer Curtains

Ad Specifications:

Sizes:

1440 x 1800 px (4:5 ratio)

1080 x 1080 px (1:1 ratio)

1080 x 1920 px (9:16 ratio for Stories/Reels)

Format: PNG (high resolution, not blurry)

Designed specifically for Meta (Facebook/Instagram ads)

Mobile-friendly layout (clear, easy to read)

Style:

Bold, sales-driven, retail-style ads (NOT minimal)

Eye-catching and designed to generate leads

Clean, professional layout

Similar to promotional home improvement ads

Brand Colours:

Red: #E31E24

Blue: #0072BC

White backgrounds

Each ad must include:

“SALE NOW ON” banner at top

Our showroom address:
214 Upper Carrow Road, Fenwick Vale (must be fully visible, not cut off)

Phone number: 9482 1576

Our logo (provided)

Badge: “Celebrating 13 YEARS in Business” (must be clean and readable)

Call to Action:

For 5 ads: “Book a FREE quote TODAY!”

For Security Doors ad: “ORDER NOW”

Offers / Pricing:

Most products: “UP TO 40% OFF”

Plantation Shutters: “FROM $299/sqm”

Security Doors: “FROM $750”

Content for each ad (examples):

Veltrashade Blinds:

Made to Measure

Fully Installed

Wind, Sun & Insect Protection

Outdoor Awnings:

Reduce Heat & Glare

Energy Saving

Custom Made

Plantation Shutters:

Modern & Elegant

Light & Privacy Control

Durable & Easy Care

Roller Shutters:

Security Protection

Block Heat & Noise

Total Light Control

Security Doors:

3 Point Locking

Premium Mesh

Custom Made

Blinds & Sheers:

Huge Range of Fabrics

Modern Soft Finish

Perfect for Any Room

Important Notes:

All text must be sharp and easy to read (no blur)

Layout must be balanced and not overcrowded

Ensure no text is cut off (especially address and headings)

Badge text must be straight and professional (no distortion)

Use high-quality, relevant images (we will provide references)

Goal:
Create ads that look professional, trustworthy, and generate enquiries/bookings for in-home quotes.

We are open to creative ideas but want a strong, bold retail-style ad that converts.
I have uploaed chatgpt mocks

Target Market(s)

Homeowners in Melbourne, Australia (typically aged 30–65) looking to improve their homes with blinds, shutters, awnings and security doors. Mid to high income households focused on quality, security, and modern home upgrades.

Industry/Entity Type

Home Improvement / Construction / Retail

Font styles to use
Sans Serif

Requirements
Must have
• Clear, bold and easy-to-read text (must be readable on mobile) High-quality, non-blurry design Strong “SALE” style layout (retail promotional look) Proper spacing (no overcrowded designs) All key info visible (address must NOT be cut off) Correct pricing and offers included Clean “13 YEARS” badge (no distortion or curved text) Consistent branding across all 6 ads
Nice to have
• Modern, slightly premium feel while still being bold Good use of contrast (red/blue/white) Subtle shadows or layering to improve depth Clean use of icons or bullet points Strong hierarchy (headline → benefits → offer → CTA) Variations in layout for testing different ad styles
Should not have
• Minimal or plain designs (we want bold, sales-driven ads) Hard-to-read fonts or script fonts Low-quality or blurry images Overcrowded layouts with too much text Important text cut off (especially address or headings) Overuse of effects or “cheap” looking graphics Yellow-heavy colour schemes (must follow brand colours)

```html
<!DOCTYPE html>
<html lang="en">
<head>
<meta charset="utf-8">
<title>Panes Screens &amp; Louvres – Veltrashade Blinds Sale</title>
<link rel="stylesheet" href="https://fonts.googleapis.com/css2?family=Lexend:wght@500&family=Oswald:wght@700&family=Poppins:wght@400;600;700;800&family=Roboto:wght@500;900&display=swap">
<style>
  :root {
    --brand-red: #f3111b;
    --brand-blue: #1580cf;
    --deep-blue: #1c4c8c;
    --white: #ffffff;
    --sky-top: #cfe6f6;
    --sky-mid: #eef5fa;
    --photo-dark: #46443f;
    --photo-blue: #2f4fa8;
  }
  * { margin: 0; padding: 0; box-sizing: border-box; }
  html, body { width: 960px; height: 1200px; overflow: hidden; background: var(--white); }
  .ad {
    position: relative;
    width: 960px;
    height: 1200px;
    overflow: hidden;
    font-family: "Poppins", sans-serif;
    background: var(--white);
  }
  .backdrop {
    position: absolute; inset: 0 0 180px 0;
    background: linear-gradient(180deg, var(--sky-top) 0%, var(--sky-mid) 45%, #e6eaee 75%, var(--white) 100%);
  }

  /* Header */
  .brand {
    position: absolute; left: 102px; top: 34px;
    display: flex; align-items: center; gap: 14px;
  }
  .brand-mark { width: 44px; height: 44px; background: var(--brand-red); }
  .brand-name {
    font-weight: 700; font-size: 29px; color: var(--brand-blue);
    letter-spacing: -0.3px; line-height: 1;
  }
  .book-button {
    position: absolute; left: 553px; top: 33px; width: 320px; height: 47px;
    border-radius: 5px; overflow: hidden; display: flex; align-items: center;
    background: var(--brand-blue);
    text-decoration: none;
  }
  .book-button-label {
    padding-left: 14px; color: var(--white);
    font-weight: 700; font-size: 16.5px; letter-spacing: -0.2px; white-space: nowrap;
  }
  .book-button-arrow {
    position: absolute; right: 0; top: 0; width: 60px; height: 47px;
    background: var(--brand-red);
    clip-path: polygon(14px 0, 100% 0, 100% 100%, 0 100%);
    display: flex; align-items: center; justify-content: center;
  }

  /* Headlines */
  .product-band {
    position: absolute; left: 0; top: 109px; width: 960px; height: 74px;
    background: var(--brand-red);
    display: flex; align-items: center; justify-content: center;
  }
  .product-band h1 {
    color: var(--white); font-weight: 800; font-size: 52px;
    letter-spacing: 4px; line-height: 1;
  }
  .sale-headline {
    position: absolute; left: 0; top: 200px; width: 960px; text-align: center;
    font-family: "Roboto", sans-serif; font-weight: 900; font-size: 106px;
    letter-spacing: -4px; line-height: 1;
  }
  .sale-headline .sale { color: var(--brand-red); }
  .sale-headline .on { color: var(--brand-blue); }

  /* Offer pelmet + product window */
  .offer-pelmet {
    position: absolute; left: 148px; top: 314px; width: 669px; height: 72px;
    background: linear-gradient(180deg, #ffffff 0%, #f1f2f3 70%, #dcdfe2 100%);
    box-shadow: 0 4px 8px rgba(0,0,0,.18);
    display: flex; align-items: center; justify-content: center; z-index: 3;
  }
  .offer-text {
    font-family: "Roboto", sans-serif; font-weight: 500; font-size: 52px;
    color: var(--brand-red); letter-spacing: -0.5px; line-height: 1;
  }
  .offer-text .percent {
    font-family: "Poppins", sans-serif; font-weight: 800; color: var(--brand-blue);
    letter-spacing: -2px;
  }
  .window-frame {
    position: absolute; left: 160px; top: 386px; width: 646px; height: 540px;
    background: linear-gradient(90deg, #f4f5f6, #ffffff 10%, #ffffff 90%, #eceef0);
    box-shadow: 0 6px 14px rgba(0,0,0,.15);
  }
  .product-photo {
    position: absolute; left: 188px; top: 390px; width: 589px; height: 502px;
    background: linear-gradient(180deg, var(--photo-dark) 0%, #4a5070 55%, var(--photo-blue) 100%);
  }

  /* Anniversary badge */
  .anniversary-badge {
    position: absolute; left: 706px; top: 781px; width: 150px; height: 150px;
    border-radius: 50%; background: var(--white);
    box-shadow: 0 4px 10px rgba(0,0,0,.2);
    display: flex; align-items: center; justify-content: center; z-index: 4;
  }
  .badge-core {
    width: 136px; height: 136px; border-radius: 50%;
    background: var(--brand-blue); border: 3px solid var(--white);
    outline: 2px solid var(--brand-blue);
    display: flex; flex-direction: column; align-items: center; justify-content: center;
    color: var(--white); text-align: center; line-height: 1;
  }
  .badge-small { font-weight: 600; font-size: 10px; letter-spacing: 1.5px; }
  .badge-number { font-weight: 700; font-size: 44px; margin: 3px 0 0; }
  .badge-years { font-weight: 600; font-size: 12px; letter-spacing: 2px; margin-bottom: 4px; }

  /* Benefits */
  .benefits { position: absolute; left: 0; top: 958px; width: 960px; height: 75px; }
  .benefit-icon { position: absolute; top: 0; }
  .benefit-label {
    position: absolute; top: 6px;
    font-family: "Lexend", sans-serif; font-weight: 500; font-size: 23px;
    line-height: 1.15; color: var(--deep-blue); white-space: nowrap;
  }

  /* Footer */
  .phone-block {
    position: absolute; left: 0; top: 1072px; width: 457px; height: 128px;
    background: var(--brand-red);
    display: flex; align-items: center; justify-content: center;
  }
  .phone-number {
    font-family: "Oswald", sans-serif; font-weight: 700; font-size: 86px;
    color: var(--white); line-height: 1;
  }
  .address-frame {
    position: absolute; left: 462px; top: 1065px; width: 136px; height: 135px;
    border-top: 3px solid var(--brand-blue); border-left: 3px solid var(--brand-blue);
  }
  .address-block {
    position: absolute; left: 472px; top: 1073px; width: 488px; height: 127px;
    background: var(--brand-blue); color: var(--white);
    padding: 26px 0 0 36px;
  }
  .address-title { font-weight: 700; font-size: 17px; line-height: 1.25; }
  .address-line { font-weight: 400; font-size: 17px; line-height: 1.35; }
  .address-web { font-weight: 400; font-size: 17px; margin-top: 6px; }
</style>
</head>
<body>
<main class="ad">
  <div class="backdrop" role="img" aria-label="Hazy city skyline under a light blue sky with insects flying around the window"></div>

  <header>
    <div class="brand">
      <span class="brand-mark"></span>
      <span class="brand-name">Panes Screens &amp; Louvres</span>
    </div>
    <a class="book-button" href="#">
      <span class="book-button-label">Book a FREE quote TODAY!</span>
      <span class="book-button-arrow">
        <svg width="18" height="26" viewBox="0 0 18 26"><path d="M4 3 L14 13 L4 23" fill="none" stroke="#fff" stroke-width="3.5" stroke-linecap="round" stroke-linejoin="round"/></svg>
      </span>
    </a>
  </header>

  <div class="product-band"><h1>VELTRASHADE BLINDS</h1></div>
  <h2 class="sale-headline"><span class="sale">SALE NOW</span> <span class="on">ON!</span></h2>

  <div class="window-frame"></div>
  <div class="offer-pelmet">
    <p class="offer-text">*UP TO <span class="percent">40%</span> OFF*</p>
  </div>
  <div class="product-photo" role="img" aria-label="Photo of a dark mesh outdoor screen blind half lowered over a living room with a white sofa"></div>

  <div class="anniversary-badge">
    <div class="badge-core">
      <span class="badge-small">CELEBRATING</span>
      <span class="badge-number">13</span>
      <span class="badge-years">YEARS</span>
      <span class="badge-small">ANNIVERSARY</span>
    </div>
  </div>

  <section class="benefits">
    <div class="benefit">
      <svg class="benefit-icon" style="left:75px" width="58" height="64" viewBox="0 0 58 64">
        <ellipse cx="27" cy="14" rx="24" ry="11" fill="none" stroke="#f3111b" stroke-width="5"/>
        <ellipse cx="27" cy="14" rx="9" ry="4" fill="#f3111b"/>
        <path d="M3 14 V36 C3 44 14 48 27 48 C40 48 51 44 51 36 V14" fill="#f3111b"/>
        <path d="M30 46 L50 34 L56 46 L36 60 Z" fill="#f3111b"/>
        <path d="M38 48 l3 4 M43 45 l3 4 M48 42 l3 4" stroke="#fff" stroke-width="2"/>
      </svg>
      <p class="benefit-label" style="left:161px">Made to<br>Measure</p>
    </div>
    <div class="benefit">
      <svg class="benefit-icon" style="left:347px" width="64" height="64" viewBox="0 0 64 64">
        <circle cx="22" cy="24" r="11" fill="#f3111b"/>
        <g stroke="#f3111b" stroke-width="3.5" stroke-linecap="round">
          <path d="M22 4 v5 M22 39 v5 M2 24 h5 M37 24 h3 M8 10 l4 4 M32 34 l3 3 M8 38 l4 -4 M32 14 l4 -4"/>
        </g>
        <path d="M45 22 L62 28 V40 C62 51 54 58 45 62 C36 58 28 51 28 40 V28 Z" fill="#fff" stroke="#f3111b" stroke-width="4"/>
        <path d="M45 31 L54 34 V41 C54 46 50 50 45 52 C40 50 36 46 36 41 V34 Z" fill="none" stroke="#f3111b" stroke-width="3"/>
      </svg>
      <p class="benefit-label" style="left:432px">Wind, Sun &amp;<br>Insect Protection</p>
    </div>
    <div class="benefit">
      <svg class="benefit-icon" style="left:699px" width="50" height="64" viewBox="0 0 50 64">
        <rect x="4" y="4" width="42" height="56" fill="none" stroke="#f3111b" stroke-width="4"/>
        <circle cx="4" cy="4" r="3" fill="#f3111b"/><circle cx="46" cy="4" r="3" fill="#f3111b"/>
        <rect x="4" y="10" width="42" height="20" fill="#f3111b"/>
        <path d="M4 16 h42 M4 22 h42" stroke="#fff" stroke-width="2"/>
        <rect x="10" y="38" width="13" height="16" fill="#f3111b"/>
        <rect x="27" y="38" width="13" height="16" fill="#f3111b"/>
        <path d="M11 52 l11 -12 M28 52 l11 -12" stroke="#fff" stroke-width="2"/>
      </svg>
      <p class="benefit-label" style="left:775px">Fully<br>Installed</p>
    </div>
  </section>

  <footer>
    <div class="phone-block"><p class="phone-number">94821576</p></div>
    <div class="address-frame"></div>
    <div class="address-block">
      <p class="address-title">Showroom Address</p>
      <p class="address-line">214 Upper Carrow Road, Fenwick Vale</p>
      <p class="address-web">www.panesscreensandlouvres.com.au</p>
    </div>
  </footer>
</main>
</body>
</html>
```